Business Card For Life Coaching Business For Men

Take my existing logo and apply it to a business card. I would like the logo to be prominent with stylistic text below reading Life Coaching For Men. Contact info should show as:
Gideon Marsh
gideon@bravepathgrowth.com

```html
<!DOCTYPE html>
<html lang="en">
<head>
<meta charset="utf-8">
<title>Brave Path – Business Card</title>
<link rel="stylesheet" href="https://fonts.googleapis.com/css2?family=Barlow+Condensed:wght@400;500;600;700&display=swap">
<style>
  :root {
    --page-bg: #d3d4d6;
    --navy: #2b2a7e;
    --teal: #058383;
    --white: #ffffff;
  }
  * { margin: 0; padding: 0; box-sizing: border-box; }
  html, body {
    width: 900px; height: 1200px; overflow: hidden;
    background: var(--page-bg);
    font-family: "Barlow Condensed", sans-serif;
  }
  .card {
    position: absolute;
    left: 134px;
    width: 632px;
    height: 364px;
  }
  .card--front {
    top: 210px;
    background: linear-gradient(90deg, var(--navy) 0%, #1f5a88 55%, var(--teal) 100%);
  }
  .card--back {
    top: 624px;
    background: var(--white);
  }

  /* Front */
  .front-mark {
    position: absolute;
    left: 36px; top: 118px;
    width: 118px; height: 118px;
    border-radius: 50%;
    background: var(--white);
  }
  .front-name {
    position: absolute;
    left: 308px; top: 106px;
    color: var(--white);
    font-weight: 600;
    font-size: 80px;
    line-height: 68px;
    letter-spacing: 0.5px;
    text-transform: uppercase;
  }
  .front-tagline {
    position: absolute;
    left: 309px; top: 250px;
    color: var(--white);
    font-weight: 500;
    font-size: 19px;
    letter-spacing: 2.2px;
    text-transform: uppercase;
  }

  /* Back */
  .back-mark {
    position: absolute;
    left: 66px; top: 140px;
    width: 86px; height: 86px;
    border-radius: 50%;
    background: var(--navy);
  }
  .back-name {
    position: absolute;
    left: 168px; top: 139px;
    color: var(--navy);
    font-weight: 600;
    font-size: 50px;
    line-height: 42px;
    text-transform: uppercase;
  }
  .divider {
    position: absolute;
    left: 316px; top: 125px;
    width: 2px; height: 117px;
    background: var(--navy);
  }
  .contact {
    position: absolute;
    left: 344px; top: 120px;
    color: var(--navy);
  }
  .contact__name {
    color: var(--teal);
    font-weight: 700;
    font-size: 27px;
    line-height: 28px;
    letter-spacing: 0.6px;
    text-transform: uppercase;
  }
  .contact__role {
    font-size: 18px;
    line-height: 22px;
    margin-bottom: 6px;
  }
  .contact__line {
    display: flex;
    align-items: center;
    gap: 8px;
    font-size: 18px;
    line-height: 23px;
  }
  .contact__icon { width: 16px; height: 16px; flex: none; }
  .contact__phone { letter-spacing: 1.2px; }
</style>
</head>
<body>

<section class="card card--front">
  <div class="front-mark" aria-hidden="true"></div>
  <div class="front-name">Brave<br>Path</div>
  <div class="front-tagline">Life Coaching for Men</div>
</section>

<section class="card card--back">
  <div class="back-mark" aria-hidden="true"></div>
  <div class="back-name">Brave<br>Path</div>
  <div class="divider"></div>
  <div class="contact">
    <div class="contact__name">Gideon Marsh</div>
    <div class="contact__role">Owner</div>
    <div class="contact__line contact__phone">
      <svg class="contact__icon" viewBox="0 0 24 24"><path fill="#058383" d="M6.6 10.8a15.2 15.2 0 0 0 6.6 6.6l2.2-2.2c.3-.3.7-.4 1-.2 1.1.4 2.3.6 3.6.6.6 0 1 .4 1 1V20c0 .6-.4 1-1 1A17 17 0 0 1 3 4c0-.6.4-1 1-1h3.5c.6 0 1 .4 1 1 0 1.3.2 2.5.6 3.6.1.3 0 .7-.2 1z"/></svg>
      <span>(555)014-2736</span>
    </div>
    <div class="contact__line">
      <svg class="contact__icon" viewBox="0 0 24 24"><rect x="2" y="5" width="20" height="14" fill="#058383"/><path d="M2 5l10 8 10-8M2 19l8-7M22 19l-8-7" stroke="#fff" stroke-width="1.6" fill="none"/></svg>
      <span>gideon@bravepathgrowth.com</span>
    </div>
    <div class="contact__line">
      <svg class="contact__icon" viewBox="0 0 24 24" fill="none" stroke="#058383" stroke-width="1.8"><circle cx="12" cy="12" r="9.5"/><ellipse cx="12" cy="12" rx="4" ry="9.5"/><path d="M2.5 12h19M4 7h16M4 17h16"/></svg>
      <span>www.bravepathgrowth.com</span>
    </div>
  </div>
</section>

</body>
</html>
```